GLOW AT NINE (EP) FOR KEMURO, AN ARTISTE SIGNED TO HARBOUR MELODIES

A CREATIVELY SIMPLE EVERGREEN DESIGN. BECAUSE NO PICTURE IS REQUIRED, THE DESIGN HAS TO BE VERY EYE CATCHING AND COLOURFUL AND I WANT THE BEST CONCEPT TO DESCRIBE THE TITLE.

DETAILS TO BE USED ON THE DESIGN AS FOLLOWS

RECORDING LABEL: HARBOUR MELODIES
ARTISTE NAME: KEMURO
EP TITLE: GLOW AT NINE
TRACK LIST
1. ENI BABAWO (Produced by Kunle)
2. GROOVE PARADE (Produced by K.O.R Sounds)
3. E DON SWEET (PRODUCED BY B'KEYS)
4. IF THE RAIN COMES TONIGHT SO (PRODUCED BY SLIMMY JAY)
5. RISE SHINE GLOW (PRODUCED BY MIXXA)

ALL SONGS MIXED BY BAYO KNOBS.

Target Market(s)

AFRICA

Font styles to use
Serif
Sans Serif
Decorative
Script

Colors

Designer to choose colors to be used in the design.

Requirements
Must have
• A CREATIVELY SIMPLE EVERGREEN DESIGN
Nice to have
Should not have
• NON

```html
<!DOCTYPE html>
<html lang="en">
<head>
<meta charset="utf-8">
<title>Glow at Nine – Tracklist</title>
<link rel="stylesheet" href="https://fonts.googleapis.com/css2?family=Oswald:wght@400;500;700&family=Open+Sans:wght@300;400&family=Tinos&family=Architects+Daughter&family=Mrs+Saint+Delafield&family=Caveat:wght@400&family=Kalam:wght@300&display=swap">
<style>
  :root {
    --wall-light: #f1f1f1;
    --wall-mid: #e2e2e2;
    --heading-grey: #aaaaaa;
    --ink: #111111;
    --ink-soft: #333333;
    --credit-grey: #8e8e8e;
    --credit-light: #a6a6a6;
    --signature: #555555;
    --night: #1b1b1b;
    --night-panel: #141414;
    --glow-amber: #ffab00;
    --glow-ember: #d9480f;
    --white: #ffffff;
  }
  * { margin: 0; padding: 0; box-sizing: border-box; }
  html, body { width: 1200px; height: 1200px; overflow: hidden; background: var(--white); }
  .cover { position: relative; width: 1200px; height: 1200px; overflow: hidden; }

  .room { position: absolute; left: 0; top: 0; width: 1200px; height: 784px; }

  .tracklist-card {
    position: absolute; left: 143px; top: 366px; width: 562px; height: 307px;
    background: linear-gradient(180deg, #fbfbfb 0%, #ececec 55%, #d9d9d9 100%);
    box-shadow: 3px 4px 6px rgba(0,0,0,0.35);
  }
  .track { position: absolute; left: 42px; font-family: 'Oswald', sans-serif; font-weight: 700; font-size: 27px; color: var(--ink); line-height: 1; white-space: nowrap; letter-spacing: -0.3px; }
  .track .credit { font-family: 'Open Sans', sans-serif; font-weight: 300; font-size: 17px; color: var(--ink-soft); letter-spacing: 0; margin-left: 6px; }
  .track .credit.block { display: block; margin: 8px 0 0 0; }

  .producers { position: absolute; left: 0; top: 0; width: 1200px; height: 784px; pointer-events: none; }

  .night { position: absolute; left: 0; top: 784px; width: 1200px; height: 416px; }
  .artiste { position: absolute; left: 170px; top: 842px; font-family: 'Oswald', sans-serif; font-weight: 500; font-size: 24px; letter-spacing: 8px; color: var(--white); line-height: 1; }
  .mix-credit { position: absolute; left: 0; width: 1180px; top: 1124px; text-align: center; color: var(--white); white-space: nowrap; }
  .mix-credit .lead { font-family: 'Tinos', serif; font-size: 30px; letter-spacing: 0.5px; }
  .mix-credit .engineer { font-family: 'Oswald', sans-serif; font-weight: 700; font-size: 34px; }

  .label-mark { position: absolute; left: 1004px; top: 880px; width: 112px; text-align: center; }
  .label-mark .dot { width: 90px; height: 90px; margin: 0 auto 12px; border-radius: 50%; background: var(--glow-amber); }
  .label-mark .name { font-family: 'Oswald', sans-serif; font-weight: 500; font-size: 15px; color: var(--white); line-height: 1.1; }
</style>
</head>
<body>
<main class="cover">

  <svg class="room" width="1200" height="784" viewBox="0 0 1200 784">
    <defs>
      <linearGradient id="backWall" x1="0" y1="0" x2="0" y2="1">
        <stop offset="0" stop-color="#e6e6e6"/>
        <stop offset="0.45" stop-color="#efefef"/>
        <stop offset="1" stop-color="#e4e4e4"/>
      </linearGradient>
      <linearGradient id="sideWall" x1="0" y1="0" x2="1" y2="0">
        <stop offset="0" stop-color="#e2e2e2"/>
        <stop offset="1" stop-color="#f0f0f0"/>
      </linearGradient>
      <linearGradient id="floorShade" x1="0" y1="0" x2="0" y2="1">
        <stop offset="0" stop-color="#f2f2f2"/>
        <stop offset="1" stop-color="#e6e6e6"/>
      </linearGradient>
    </defs>
    <rect class="wall-back" width="1200" height="784" fill="url(#backWall)"/>
    <polygon class="wall-left" points="0,240 70,300 70,700 0,720" fill="#e8e8e8"/>
    <rect class="wall-inner" x="70" y="300" width="708" height="400" fill="#f4f4f4"/>
    <polygon class="wall-right" points="778,250 892,250 892,784 778,700" fill="url(#sideWall)"/>
    <rect class="wall-far-right" x="892" y="0" width="308" height="784" fill="#ececec"/>
    <polygon class="floor" points="0,720 70,700 778,700 892,784 0,784" fill="url(#floorShade)"/>
    <line x1="70" y1="700" x2="778" y2="700" stroke="#9a9a9a" stroke-width="1.5"/>
    <line x1="0" y1="722" x2="70" y2="702" stroke="#b5b5b5" stroke-width="1.2"/>
    <line x1="778" y1="702" x2="888" y2="782" stroke="#b5b5b5" stroke-width="1.2"/>
    <text class="tracklist-heading" x="168" y="293" textLength="515" lengthAdjust="spacingAndGlyphs"
          font-family="Oswald, sans-serif" font-weight="500" font-size="146" fill="var(--heading-grey)">TRACKLIST</text>
  </svg>

  <section class="tracklist-card">
    <p class="track" style="top:20px">Eni Babawo<span class="credit">(produced by KUNLE)</span></p>
    <p class="track" style="top:74px">Groove parade <span class="credit">(produced by K.O.R SOUNDS)</span></p>
    <p class="track" style="top:129px">E Don Sweet <span class="credit">(produced by B'KEYS)</span></p>
    <p class="track" style="top:178px">If the Rain Comes Tonight So<span class="credit block">(produced by SLIMMY JAY)</span></p>
    <p class="track" style="top:258px">Rise Shine Glow <span class="credit">(produced by MIXXA)</span></p>
  </section>

  <svg class="producers" width="1200" height="784" viewBox="0 0 1200 784">
    <text class="producer producer--kor" x="916" y="478" textLength="242" lengthAdjust="spacingAndGlyphs"
          font-family="'Architects Daughter', cursive" font-size="36" fill="var(--ink)">K.O.R Sounds</text>
    <text class="producer producer--mixxa" transform="translate(914,500) rotate(90)" textLength="164" lengthAdjust="spacingAndGlyphs"
          font-family="Oswald, sans-serif" font-weight="400" font-size="56" fill="var(--credit-grey)">MIXXA</text>
    <text class="producer producer--kunle" x="990" y="566" textLength="170" lengthAdjust="spacingAndGlyphs"
          font-family="'Mrs Saint Delafield', cursive" font-size="68" fill="var(--signature)">Kunle</text>
    <text class="producer producer--bkeys" x="978" y="622" textLength="190" lengthAdjust="spacingAndGlyphs"
          font-family="Caveat, cursive" font-style="italic" font-size="44" fill="var(--credit-grey)">B'KEYS</text>
    <text class="producer producer--slimmy" x="972" y="684" textLength="196" lengthAdjust="spacingAndGlyphs"
          font-family="Kalam, cursive" font-weight="300" font-style="italic" font-size="46" fill="var(--credit-light)">SLIMMY JAY</text>
  </svg>

  <svg class="night" width="1200" height="416" viewBox="0 0 1200 416">
    <rect width="1200" height="416" fill="var(--night)"/>
    <rect x="32" y="18" width="352" height="296" fill="var(--night-panel)" stroke="#2a2a2a"/>
    <polygon points="440,60 480,80 480,300 440,340" fill="#171717"/>
    <polygon points="880,110 950,80 950,330 880,300" fill="#151515"/>
    <rect x="960" y="70" width="200" height="300" fill="#181818"/>
    <rect role="img" aria-label="Dark silhouette artwork of the artiste behind the title" x="100" y="50" width="780" height="300" fill="#161616"/>
    <rect role="img" aria-label="Dark silhouette artwork of a face beside the label name" x="1040" y="80" width="140" height="300" fill="#161616"/>
    <text x="168" y="240" textLength="712" lengthAdjust="spacingAndGlyphs"
          font-family="Oswald, sans-serif" font-weight="500" font-size="176">
      <tspan fill="var(--glow-amber)">GLOW </tspan><tspan fill="var(--glow-ember)">AT</tspan><tspan fill="var(--glow-amber)"> NINE</tspan>
    </text>
  </svg>

  <p class="artiste">KEMURO</p>

  <div class="label-mark">
    <div class="dot"></div>
    <p class="name">HARBOUR MELODIES</p>
  </div>

  <p class="mix-credit"><span class="lead">ALL SONGS MIXED BY </span><span class="engineer">BAYO KNOBS</span></p>

</main>
</body>
</html>
```